Flyer für Immobilienmakler
Zielgruppe
Wir, die Wendtal Immobilien GmbH, vermitteln Häuser, Wohnungen und Grundstücke, unsere Zielgruppe sind Verkäufer und Kaufinteressenten aus der Region, Immobilien zur Vermittlung gesucht
Aufgabenstellung
Unverbindliche Ersteinschätzung, Ansprechpartner vor Ort, regionale Marktkenntnis. Max. Din A 5, Immobilien zur Vermittlung gesucht.
- Flyer nur zur Immobilienvermittlung

```html
<!DOCTYPE html>
<html lang="de">
<head>
<meta charset="utf-8">
<title>Wendtal Immobilien GmbH – Flyer Immobilienvermittlung</title>
<link rel="stylesheet" href="https://fonts.googleapis.com/css2?family=Anton&family=Figtree:wght@400;600;700;800&display=swap">
<style>
  :root {
    --purple: #6a4fa3;
    --purple-dark: #4c3680;
    --green: #17986b;
    --ink: #1c1c1c;
    --black: #050505;
    --white: #ffffff;
    --grey-soft: #ececec;
    --stage: #e4e1dc;
  }
  * { box-sizing: border-box; margin: 0; padding: 0; }
  html, body { width: 1200px; height: 1117px; overflow: hidden; background: var(--stage); }
  .flyer {
    position: absolute; left: 225px; top: 28px; width: 750px; height: 1060px;
    background: var(--white); overflow: hidden; font-family: "Figtree", sans-serif; color: var(--ink);
  }
  .shapes { position: absolute; inset: 0; width: 750px; height: 1060px; }
  .photo { position: absolute; }
  .photo-house {
    left: 375px; top: 0; width: 375px; height: 405px;
    background: linear-gradient(180deg, #7fb6e6 0%, #b9d8f0 35%, #dfe6e4 55%, #6f9a55 80%, #8db45f 100%);
    clip-path: polygon(0 0, 100% 0, 100% 78%, 50% 100%, 0 78%);
  }
  .photo-clients {
    left: 0; top: 675px; width: 375px; height: 385px;
    background: linear-gradient(135deg, #b08466 0%, #8a5a3c 40%, #c89c7a 65%, #6e4a35 100%);
    clip-path: polygon(0 0, 100% 35%, 100% 100%, 0 100%);
  }
  .brand { position: absolute; left: 52px; top: 100px; width: 270px; text-align: center; }
  .brand-name { font-size: 17px; font-weight: 600; color: var(--ink); }
  .brand-tag { font-size: 8px; color: #333; margin-top: 4px; letter-spacing: .2px; }
  .headline {
    position: absolute; left: 52px; top: 156px; font-family: "Anton", sans-serif; font-weight: 400;
    text-transform: uppercase; letter-spacing: .6px;
  }
  .headline span { display: block; }
  .headline .small { font-size: 21px; line-height: 32px; color: var(--ink); }
  .headline .big { font-size: 38px; line-height: 43px; color: var(--ink); }
  .headline .accent { font-size: 38px; line-height: 43px; color: var(--purple); }
  .rule { position: absolute; left: 52px; width: 293px; height: 2px; background: var(--green); }
  .about { position: absolute; left: 52px; top: 352px; width: 300px; }
  .about h2 { font-size: 20px; font-weight: 700; color: var(--green); margin-bottom: 2px; }
  .about p { font-size: 14px; line-height: 18.3px; color: #333; }
  .usp { position: absolute; left: 52px; top: 560px; list-style: none; }
  .usp li { display: flex; gap: 10px; font-weight: 800; font-size: 16.5px; line-height: 21px; text-transform: uppercase; margin-bottom: 14px; letter-spacing: .2px; }
  .usp svg { flex: none; margin-top: 3px; }
  .services-title {
    position: absolute; left: 410px; top: 434px; width: 305px; height: 40px;
    background: var(--green); color: var(--white); font-family: "Anton", sans-serif; font-weight: 400;
    font-size: 25px; letter-spacing: .5px; text-align: center; line-height: 40px; box-shadow: 0 3px 0 rgba(0,0,0,.15);
  }
  .services { position: absolute; left: 413px; top: 496px; width: 318px; list-style: none; color: var(--white); }
  .services li { margin-bottom: 10px; }
  .services h3 { display: flex; align-items: center; gap: 6px; font-size: 15px; font-weight: 800; line-height: 20px; }
  .services p { font-size: 14px; line-height: 18.2px; padding-left: 19px; font-weight: 400; }
  .wanted {
    position: absolute; left: 413px; top: 776px; width: 318px;
    font-family: "Anton", sans-serif; font-weight: 400; font-size: 21px; line-height: 26px;
    letter-spacing: .4px; text-transform: uppercase; color: var(--white);
  }
  .contact { position: absolute; left: 455px; top: 952px; color: var(--white); font-style: normal; }
  .contact .row { display: flex; align-items: center; gap: 10px; }
  .contact .phone { font-family: "Anton", sans-serif; font-size: 28px; line-height: 36px; letter-spacing: .3px; }
  .contact .line { font-weight: 700; font-size: 13.5px; line-height: 21px; }
</style>
</head>
<body>
<main class="flyer">
  <svg class="shapes" viewBox="0 0 750 1060" aria-hidden="true">
    <defs>
      <linearGradient id="fade" x1="0" y1="0" x2="0" y2="1">
        <stop offset="0" stop-color="#6a4fa3"/>
        <stop offset="0.8" stop-color="#6a4fa3"/>
        <stop offset="0.93" stop-color="#050505"/>
      </linearGradient>
    </defs>
    <polygon points="245,0 375,0 375,48" fill="#ececec"/>
    <polygon points="375,0 750,0 750,1060 375,1060" fill="url(#fade)"/>
    <polygon points="375,332 565,420 750,332 750,345 565,432 375,345" fill="#4c3680"/>
    <polygon points="375,312 565,400 750,312 750,322 565,410 375,322" fill="#ffffff"/>
    <polygon points="230,745 375,690 375,760" fill="#ececec"/>
    <polygon points="162,1060 750,838 750,1060" fill="#050505"/>
    <polygon points="520,905 750,822 750,838" fill="#050505"/>
  </svg>

  <div class="photo photo-house" role="img" aria-label="Foto: weißes Einfamilienhaus mit Veranda, Bäumen und Rasen"></div>
  <div class="photo photo-clients" role="img" aria-label="Foto: lächelndes Paar beim Handschlag am Küchentisch"></div>

  <div class="brand">
    <div class="brand-name">Wendtal Immobilien GmbH</div>
    <div class="brand-tag">Vermittlung von Häusern · Wohnungen · Grundstücken</div>
  </div>

  <h1 class="headline">
    <span class="small">Ihr</span>
    <span class="big">Immobilienprofi</span>
    <span class="accent">in Wendtal &amp;</span>
    <span class="accent">Umgebung</span>
  </h1>

  <div class="rule" style="top:332px"></div>

  <section class="about">
    <h2>Über Uns</h2>
    <p>Wendtal Immobilien GmbH ist Ihr erfahrener Partner für die Vermittlung von Häusern, Wohnungen und Grundstücken in der Region. Wir begleiten Verkäufer und Kaufinteressenten mit persönlichem Service – von der ersten Bewertung bis zur Schlüsselübergabe.</p>
  </section>

  <div class="rule" style="top:528px"></div>

  <ul class="usp">
    <li><svg width="15" height="15" viewBox="0 0 16 16"><circle cx="8" cy="8" r="8" fill="#6a4fa3"/><path d="M4.5 8.3l2.3 2.2 4.7-4.8" stroke="#fff" stroke-width="2" fill="none"/></svg><span>Unverbindliche<br>Ersteinschätzung</span></li>
    <li><svg width="15" height="15" viewBox="0 0 16 16"><circle cx="8" cy="8" r="8" fill="#6a4fa3"/><path d="M4.5 8.3l2.3 2.2 4.7-4.8" stroke="#fff" stroke-width="2" fill="none"/></svg><span>Ansprechpartner vor Ort</span></li>
    <li><svg width="15" height="15" viewBox="0 0 16 16"><circle cx="8" cy="8" r="8" fill="#6a4fa3"/><path d="M4.5 8.3l2.3 2.2 4.7-4.8" stroke="#fff" stroke-width="2" fill="none"/></svg><span>Regionale Marktkenntnis</span></li>
  </ul>

  <h2 class="services-title">UNSERE LEISTUNGEN</h2>

  <ul class="services">
    <li>
      <h3><svg width="13" height="13" viewBox="0 0 16 16"><circle cx="8" cy="8" r="8" fill="#fff"/><path d="M4.5 8.3l2.3 2.2 4.7-4.8" stroke="#6a4fa3" stroke-width="2.2" fill="none"/></svg>Vermittlung von Häusern</h3>
      <p>Wir vermitteln Ihr Einfamilien-, Reihen- oder Mehrfamilienhaus an geprüfte Käufer.</p>
    </li>
    <li>
      <h3><svg width="13" height="13" viewBox="0 0 16 16"><circle cx="8" cy="8" r="8" fill="#fff"/><path d="M4.5 8.3l2.3 2.2 4.7-4.8" stroke="#6a4fa3" stroke-width="2.2" fill="none"/></svg>Vermittlung von Wohnungen</h3>
      <p>Eigentumswohnungen marktgerecht bewertet, gezielt beworben und sicher verkauft.</p>
    </li>
    <li>
      <h3><svg width="13" height="13" viewBox="0 0 16 16"><circle cx="8" cy="8" r="8" fill="#fff"/><path d="M4.5 8.3l2.3 2.2 4.7-4.8" stroke="#6a4fa3" stroke-width="2.2" fill="none"/></svg>Vermittlung von Grundstücken</h3>
      <p>Bauland und Grundbesitz in der Region – von der Bewertung bis zum Notartermin.</p>
    </li>
    <li>
      <h3><svg width="13" height="13" viewBox="0 0 16 16"><circle cx="8" cy="8" r="8" fill="#fff"/><path d="M4.5 8.3l2.3 2.2 4.7-4.8" stroke="#6a4fa3" stroke-width="2.2" fill="none"/></svg>Beratung für Kaufinteressenten</h3>
      <p>Persönliche Beratung und passende Angebote für Ihre Suche nach einem Zuhause.</p>
    </li>
  </ul>

  <p class="wanted">Immobilien zur Vermittlung gesucht!</p>

  <address class="contact">
    <div class="row phone"><svg width="16" height="18" viewBox="0 0 24 24"><path d="M6.6 10.8a15 15 0 006.6 6.6l2.2-2.2a1 1 0 011-.25 11.4 11.4 0 003.6.57 1 1 0 011 1V20a1 1 0 01-1 1A17 17 0 013 4a1 1 0 011-1h3.5a1 1 0 011 1c0 1.25.2 2.45.57 3.57a1 1 0 01-.25 1z" fill="#17986b"/></svg>+49 85 11 482630-0</div>
    <div class="row line"><svg width="16" height="16" viewBox="0 0 16 16"><circle cx="8" cy="8" r="8" fill="#17986b"/><rect x="4" y="5.2" width="8" height="5.6" fill="none" stroke="#050505" stroke-width="1"/><path d="M4 5.5l4 3 4-3" fill="none" stroke="#050505" stroke-width="1"/></svg>kontakt@wendtal-immobilien.de</div>
    <div class="row line"><svg width="16" height="18" viewBox="0 0 16 20"><path d="M8 0a7 7 0 00-7 7c0 5 7 13 7 13s7-8 7-13a7 7 0 00-7-7z" fill="#17986b"/><circle cx="8" cy="7" r="2.6" fill="#050505"/></svg>Lindenweg 12, 84300 Wendtal</div>
  </address>
</main>
</body>
</html>
```